Business Card Design Project

We need a business card to reflect the design of our website - just so it all ties in - it has a retro feel and can be found at http://www.velorasoulpair.com
We will need our phone 0437 215 964
Web address, and email velorapair@fernmail.com included
Our catch cry is "Classic Cocktail Music"
Perfect Live Music for Private & Corporate Events, Weddings and Dinner Music
Our names should be included :-
Maribel Thorne / piano & Dennis Holloway / bass
I am now also including our logo so that it can be included (in part or whole) somehow in the design
My partner thinks we should include our logo in some form in the design of the card - i will attach this here for you. I will attach eps but if you prefer another format please let me know
Regards
Mari

```html
<!DOCTYPE html>
<html lang="en">
<head>
<meta charset="UTF-8">
<title>Velora Duo – Business Card</title>
<link rel="stylesheet" href="https://fonts.googleapis.com/css2?family=Quicksand:wght@500;600;700&display=swap">
<style>
  :root {
    --stage: #161616;
    --card-teal: #93d2ce;
    --band-cream: #eee8d3;
    --ink: #4a4a47;
    --mark-dark: #3e3c3a;
    --mark-light: #f3ecd2;
    --stitch: #6aa9a5;
  }
  * { margin: 0; padding: 0; box-sizing: border-box; }
  html, body {
    width: 1200px;
    height: 790px;
    overflow: hidden;
    background: var(--stage);
    font-family: "Quicksand", sans-serif;
    color: var(--ink);
  }
  .stage {
    position: relative;
    width: 1200px;
    height: 790px;
    display: flex;
    align-items: center;
    justify-content: center;
    gap: 60px;
  }
  .card {
    position: relative;
    width: 520px;
    height: 318px;
    background: var(--card-teal);
    overflow: hidden;
  }

  /* brand block */
  .brand {
    display: flex;
    flex-direction: column;
    align-items: center;
  }
  .brand-row {
    display: flex;
    align-items: center;
    gap: 14px;
  }
  .brand-dot {
    width: 58px;
    height: 58px;
    border-radius: 50%;
    background: var(--mark-dark);
  }
  .brand-name {
    font-weight: 700;
    font-size: 30px;
    letter-spacing: 1px;
    color: var(--mark-dark);
  }
  .brand-tagline {
    margin-top: 10px;
    font-weight: 700;
    font-size: 17px;
    letter-spacing: 3px;
    text-transform: uppercase;
    color: var(--ink);
  }

  /* front */
  .card-front .brand {
    position: absolute;
    top: 78px;
    left: 0;
    right: 0;
  }
  .card-front .duo-names {
    position: absolute;
    left: 0;
    right: 0;
    bottom: 56px;
    text-align: center;
    font-size: 17px;
    font-weight: 500;
    letter-spacing: 0.3px;
  }

  /* back */
  .card-back .brand {
    position: absolute;
    top: 46px;
    left: 0;
    right: 0;
  }
  .contact-row {
    position: absolute;
    left: 22px;
    right: 22px;
    top: 188px;
    display: flex;
    justify-content: space-between;
    align-items: center;
    font-size: 13px;
    font-weight: 600;
  }
  .contact-item {
    display: flex;
    align-items: center;
    gap: 7px;
  }
  .contact-icon {
    width: 18px;
    height: 18px;
    border-radius: 50%;
    background: var(--mark-dark);
    color: var(--mark-light);
    font-size: 11px;
    font-weight: 700;
    display: flex;
    align-items: center;
    justify-content: center;
    line-height: 1;
  }
  .stitch-line {
    position: absolute;
    left: 14px;
    right: 14px;
    height: 0;
    border-top: 1px dashed var(--stitch);
  }
  .stitch-line.upper { top: 220px; }
  .service-band {
    position: absolute;
    left: 0;
    right: 0;
    bottom: 0;
    height: 82px;
    background: var(--band-cream);
    display: flex;
    align-items: center;
    justify-content: center;
  }
  .service-band .stitch-line {
    top: 8px;
    border-top-color: #c9c1a4;
  }
  .service-band .stitch-line.lower {
    top: auto;
    bottom: 8px;
  }
  .service-line {
    font-size: 14px;
    font-weight: 600;
    text-align: center;
    padding: 0 20px;
  }
</style>
</head>
<body>
<main class="stage">

  <section class="card card-front" aria-label="Business card front">
    <div class="brand">
      <div class="brand-row">
        <span class="brand-dot" aria-hidden="true"></span>
        <span class="brand-name">Velora Duo</span>
      </div>
      <p class="brand-tagline">Classic Cocktail Music</p>
    </div>
    <p class="duo-names">Maribel Thorne - Piano &amp; Dennis Holloway - Bass</p>
  </section>

  <section class="card card-back" aria-label="Business card back">
    <div class="brand">
      <div class="brand-row">
        <span class="brand-dot" aria-hidden="true"></span>
        <span class="brand-name">Velora Duo</span>
      </div>
      <p class="brand-tagline">Classic Cocktail Music</p>
    </div>

    <div class="contact-row">
      <span class="contact-item"><span class="contact-icon">w</span>www.velorasoulpair.com</span>
      <span class="contact-item"><span class="contact-icon">e</span>velorapair@fernmail.com</span>
      <span class="contact-item"><span class="contact-icon">m</span>0437 215 964</span>
    </div>
    <div class="stitch-line upper"></div>

    <div class="service-band">
      <div class="stitch-line"></div>
      <p class="service-line">Perfect Live Music for Private &amp; Corporate Events, Weddings and Dinner Music</p>
      <div class="stitch-line lower"></div>
    </div>
  </section>

</main>
</body>
</html>
```